K&T Fixit and Rebuild general contracting business card design

I already have a logo that I want to use and I need a card that uses that logo and color scheme on the front with the address phone numbers and email and on the back a place for technicians to write in their name and phone number when they hand it out. It will need the License number of License #KTFXTRB318QN.
It should say General Contractor under the company name. The address is
4417 NE 3rd Ave, Ste D246
Vancouver, WA 98612
www.kandtfixitandrebuild.example
office@kandtfixitandrebuild.example
360-555-0182 is the telephone number
360-555-0149 is the fax number

Target Market(s)

Homeowners needing remodel work or repairs in their home.

Industry/Entity Type

Construction

Contact Information for Business Card

Business name, address, phone number, license number, fax number, email, and website on the front and a place to fill in technician's name and number

Font styles to use
Serif

Requirements
Must have
• Business name, address, phone number, license number, fax number, email, and website on the front and a place to fill in technician's name and number
Nice to have
• I uploaded an example of a front that is good.
Should not have
• Froo froo or extra embellishments.

```html
<!DOCTYPE html>
<html lang="en">
<head>
<meta charset="utf-8">
<title>K&amp;T Fixit and Rebuild — Business Card</title>
<link href="https://fonts.googleapis.com/css2?family=Libre+Baskerville:wght@400;700&display=swap" rel="stylesheet">
<style>
  :root {
    --backdrop: #1c1c1c;
    --wood-light: #b08a66;
    --wood-mid: #a07a57;
    --wood-dark: #8c6a4b;
    --ink: #4a3423;
    --ink-soft: #5e4431;
    --rule: #6a4e38;
  }
  * { margin: 0; padding: 0; box-sizing: border-box; }
  html, body {
    width: 1200px; height: 1199px; overflow: hidden;
    background: var(--backdrop);
  }
  body { font-family: "Libre Baskerville", Georgia, serif; color: var(--ink); }
  .canvas { position: relative; width: 1200px; height: 1199px; }
  .card {
    position: absolute; left: 195px; width: 800px; height: 436px;
    overflow: hidden;
  }
  .card--front { top: 115px; }
  .card--back { top: 650px; }
  .card__surface {
    position: absolute; inset: 0;
    background: linear-gradient(180deg, var(--wood-light) 0%, var(--wood-mid) 35%, var(--wood-light) 60%, var(--wood-dark) 100%);
  }

  /* Company name block */
  .brand {
    position: absolute; text-align: center; line-height: 1;
    font-weight: 700; color: var(--ink);
  }
  .brand__mark { display: block; font-size: 92px; letter-spacing: 2px; }
  .brand__name { display: block; margin-top: 12px; font-size: 17px; letter-spacing: 2px; text-transform: uppercase; }
  .brand__trade { display: block; margin-top: 12px; font-size: 14px; letter-spacing: 3px; text-transform: uppercase; color: var(--ink-soft); font-weight: 400; }
  .card--front .brand { left: 40px; width: 318px; top: 120px; }
  .card--back .brand { left: 0; width: 800px; top: 42px; }
  .card--back .brand__mark { font-size: 108px; }
  .card--back .brand__name { font-size: 24px; margin-top: 14px; }
  .card--back .brand__trade { font-size: 15px; margin-top: 12px; }

  .divider {
    position: absolute; left: 375px; top: 108px; width: 1px; height: 236px;
    background: var(--rule);
  }

  /* Front contact details */
  .details { position: absolute; left: 400px; top: 100px; width: 385px; }
  .details__name {
    font-size: 23px; font-weight: 400; letter-spacing: 2px;
    text-transform: uppercase; color: var(--ink-soft); line-height: 1.1;
  }
  .details__role { font-size: 14px; font-weight: 700; margin-top: 6px; }
  .details__address { font-size: 14px; line-height: 22px; margin-top: 10px; }
  .contact { list-style: none; margin-top: 8px; font-size: 14px; }
  .contact li { display: flex; align-items: center; gap: 7px; height: 23px; white-space: nowrap; }
  .contact svg { width: 12px; height: 12px; flex: none; }
  .details__license { margin-top: 10px; font-size: 13px; font-weight: 700; letter-spacing: 0.5px; }

  /* Back write-in fields */
  .writein { position: absolute; left: 130px; width: 540px; top: 272px; }
  .writein__row { display: flex; align-items: flex-end; gap: 14px; height: 34px; margin-bottom: 26px; }
  .writein__label { font-size: 15px; font-weight: 700; letter-spacing: 1px; text-transform: uppercase; white-space: nowrap; width: 130px; }
  .writein__line { flex: 1; height: 1px; background: var(--ink); margin-bottom: 4px; }
</style>
</head>
<body>
<main class="canvas">
  <section class="card card--front">
    <div class="card__surface" role="img" aria-label="Light oak wood grain texture"></div>
    <div class="brand">
      <span class="brand__mark">K&amp;T</span>
      <span class="brand__name">Fixit and Rebuild</span>
      <span class="brand__trade">General Contractor</span>
    </div>
    <div class="divider"></div>
    <div class="details">
      <h1 class="details__name">Daniel Brooks</h1>
      <p class="details__role">Director</p>
      <p class="details__address">4417 NE 3rd Ave, Ste D246<br>Vancouver, WA 98612</p>
      <ul class="contact">
        <li><svg viewBox="0 0 12 12"><path d="M2.5 1 L4.5 1 L5 3.5 L3.8 4.5 Q5 7 7.5 8.2 L8.5 7 L11 7.5 L11 9.5 Q10.5 11 9 11 Q1 10 1 3 Q1 1.5 2.5 1Z" fill="var(--ink)"/></svg>360-555-0182</li>
        <li><svg viewBox="0 0 12 12"><rect x="3" y="1" width="6" height="3" fill="none" stroke="var(--ink)"/><rect x="1" y="4" width="10" height="5" fill="var(--ink)"/><rect x="3" y="8" width="6" height="3" fill="none" stroke="var(--ink)"/></svg>Fax 360-555-0149</li>
        <li><svg viewBox="0 0 12 12"><rect x="1" y="2.5" width="10" height="7" fill="none" stroke="var(--ink)"/><path d="M1 2.5 L6 6.5 L11 2.5" fill="none" stroke="var(--ink)"/></svg>office@kandtfixitandrebuild.example</li>
        <li><svg viewBox="0 0 12 12"><circle cx="6" cy="6" r="5" fill="none" stroke="var(--ink)"/><ellipse cx="6" cy="6" rx="2.2" ry="5" fill="none" stroke="var(--ink)"/><path d="M1 6 H11" stroke="var(--ink)"/></svg>www.kandtfixitandrebuild.example</li>
      </ul>
      <p class="details__license">License #KTFXTRB318QN</p>
    </div>
  </section>

  <section class="card card--back">
    <div class="card__surface" role="img" aria-label="Light oak wood grain texture"></div>
    <div class="brand">
      <span class="brand__mark">K&amp;T</span>
      <span class="brand__name">Fixit and Rebuild</span>
      <span class="brand__trade">General Contractor</span>
    </div>
    <div class="writein">
      <div class="writein__row"><span class="writein__label">Technician</span><span class="writein__line"></span></div>
      <div class="writein__row"><span class="writein__label">Phone</span><span class="writein__line"></span></div>
    </div>
  </section>
</main>
</body>
</html>
```